OLVAK Web Design (Need help to re-design our website)

We need someone to help us re-design our website and launch it. All contents for the website are ready. (https://olvak.example.au/)

-Rearrange categories:
1. Heating & Cooling
2. Remove Home Appliance
3. Remove Entertainment

Home page - redesign (It will be a nice touch if the banner is in the loop).

NOTE:
-Brand colour blue and orange.
-Try using professional fonts (Example: Helvetica, etc.)
-The website's Footer should be readable and use light colour.

Target Market(s)

Residentials & commercial buildings

Industry/Entity Type

Heat Ventilation and Cooling Industry, Technology , Renewables

Coding

Coded - Design and coding required

Colors
0094D4
00A9DD
6FCCEA
C7EBF8
E9F6FB
59FF00
82FF00
B8FF75
E3FFCB
F4FFEA
F0912C
F2A743
F7CA91
FBE8D2
FDF5EE

Requirements
Nice to have
• Effects/transition on the words/copy/images.

```html
<!DOCTYPE html>
<html lang="en">
<head>
<meta charset="utf-8">
<title>OLVAK — Heating &amp; Cooling</title>
<link href="https://fonts.googleapis.com/css2?family=Lato:wght@300;400;700;900&family=Montserrat:wght@500;600;700;800&family=Oswald:wght@500&display=swap" rel="stylesheet">
<style>
:root{
  --navy:#0c2a5b;
  --navy-deep:#0a2350;
  --blue:#1760b0;
  --blue-mid:#1d4f9a;
  --orange:#f39322;
  --ink:#1c1c1c;
  --muted:#555;
  --line:#d4d8de;
  --white:#ffffff;
}
*{margin:0;padding:0;box-sizing:border-box}
html,body{width:1200px;height:3756px;overflow:hidden}
body{position:relative;font-family:"Lato",sans-serif;color:var(--ink);background:var(--white)}
.abs{position:absolute}
a{color:inherit;text-decoration:none}

/* top bar */
.topbar{left:0;top:0;width:1200px;height:34px;background:var(--navy)}
.topbar .contact{top:8px;font-size:13px;color:#e6ecf5;display:flex;align-items:center;gap:8px}
.topbar .staff{left:816px;top:0;width:384px;height:34px;background:var(--orange);clip-path:polygon(28px 0,100% 0,100% 100%,0 100%)}
.topbar .staff span{position:absolute;left:48px;top:9px;font:700 13px "Montserrat",sans-serif;color:#fff;display:flex;gap:8px;align-items:center}
.topbar .social{top:7px;width:20px;height:20px;border-radius:50%;background:#fff}

/* header */
.header{left:0;top:34px;width:1200px;height:94px;background:#fff}
.brand{display:flex;align-items:center;gap:12px;font:700 44px "Montserrat",sans-serif;letter-spacing:6px;color:var(--blue)}
.brand .mark{width:30px;height:30px;background:var(--orange)}
.nav a{position:absolute;top:38px;font:600 13px "Montserrat",sans-serif;color:#333}
.nav a.active{color:var(--blue)}
.nav a.active::after{content:"";position:absolute;left:0;right:0;top:28px;height:2px;background:var(--orange)}
.btn-book{left:988px;top:27px;width:175px;height:41px;background:var(--blue);color:#fff;font:600 13px "Montserrat",sans-serif;display:flex;align-items:center;justify-content:center}

/* hero */
.hero{left:0;top:128px;width:1200px;height:659px;overflow:hidden;border-radius:0 0 50% 50%/0 0 80px 80px;background:linear-gradient(180deg,#1b3f80 0%,#13306a 55%,#0d2757 100%)}
.hero h1{left:106px;top:115px;font:300 70px "Lato",sans-serif;color:#fff;line-height:1}
.hero h1 b{font-weight:900;color:var(--orange)}
.hero h2{left:106px;top:200px;font:700 52px "Montserrat",sans-serif;color:#fff;letter-spacing:1px}
.btn-orange{background:var(--orange);color:#fff;font:700 13px "Montserrat",sans-serif;display:flex;align-items:center;justify-content:center}
.hero .btn-orange{left:108px;top:292px;width:130px;height:47px}
.hero .product{left:736px;top:54px;width:314px;height:525px;border-radius:14px;background:linear-gradient(90deg,#cfd4da,#f4f5f7 45%,#d6dadf)}

/* about */
.about{left:0;top:787px;width:1200px;height:693px;background:linear-gradient(180deg,#fff 0%,#fff 30%,#e4e5e8 100%)}
.about .photo{left:85px;top:121px;width:418px;height:426px;background:linear-gradient(135deg,#e9ecef,#b7bcc3 60%,#2d3440)}
.about .eyebrow{left:565px;top:106px;font:400 15px "Lato",sans-serif;color:#777}
.about .brand{left:561px;top:136px;font-size:58px}
.about .brand .mark{width:36px;height:36px}
.about p{left:563px;top:206px;width:576px;font-size:13px;line-height:26.5px;color:#222}
.about .rebate{left:589px;top:378px;font:700 17px "Lato",sans-serif;color:var(--orange)}
.badge{top:430px;border-radius:50%}

/* heating & cooling */
.solutions-bg{left:0;top:1480px;width:1200px;height:576px;background:linear-gradient(180deg,#1f3f85 0%,#17336e 60%,#13306a 100%)}
.solutions .eyebrow{left:0;width:1200px;top:1572px;text-align:center;font:400 25px "Lato",sans-serif;color:var(--orange)}
.solutions h2{left:0;width:1200px;top:1612px;display:flex;justify-content:center;align-items:center;gap:14px;font:700 52px "Montserrat",sans-serif;color:#fff}
.solutions h2 .mark{width:30px;height:30px;background:var(--orange)}
.solutions .lead{left:0;width:1200px;top:1682px;text-align:center;font:300 22px "Lato",sans-serif;color:#fff}
.card{left:68px;top:1776px;width:1040px;height:805px;background:#fff}
.tile{position:absolute;width:442px;height:251px}
.tile-label{position:absolute;width:442px;text-align:center;font:400 23px "Lato",sans-serif;color:#222}

/* testimonials & quote */
.testimonials{left:0;top:2700px;width:1200px;height:624px;background:var(--navy)}
.testimonials .eyebrow{left:67px;top:59px;font:500 13px "Montserrat",sans-serif;color:#fff}
.testimonials h3{left:67px;top:81px;width:480px;font:700 37px "Montserrat",sans-serif;line-height:43px;color:#fff}
.testimonials .rule{left:67px;top:177px;width:53px;height:4px;background:var(--orange)}
.quote-item .avatar{position:absolute;width:88px;height:88px;border-radius:50%;background:linear-gradient(180deg,#d9c7b4,#8a7464);border:3px solid #fff}
.quote-item .name{position:absolute;font:700 15px "Montserrat",sans-serif;color:#fff}
.quote-item p{position:absolute;width:368px;font-size:14px;line-height:26.5px;color:#dfe5f0;text-align:justify}
.testimonials .divider{left:55px;top:369px;width:490px;height:1px;background:#3a5585}
.quote-head{left:783px;top:2700px;width:410px;height:107px;background:var(--orange)}
.quote-head small{position:absolute;left:31px;top:30px;font:400 15px "Lato",sans-serif;color:#fff}
.quote-head strong{position:absolute;left:29px;top:49px;font:500 29px "Oswald",sans-serif;color:#fff;letter-spacing:.5px}
.quote-form{left:586px;top:2807px;width:614px;height:517px;background:#fff}
.quote-form p{position:absolute;left:38px;top:50px;width:540px;font-size:13px;line-height:25px;color:#444}
.field{position:absolute;border:1px solid var(--line);background:#fff;font:400 13px "Lato",sans-serif;color:#666;padding:20px 22px}
.quote-form .btn-orange{position:absolute;left:26px;top:436px;width:203px;height:54px}

/* footer */
.footer{left:0;top:3324px;width:1200px;height:432px;background:linear-gradient(180deg,#0f2e62,#0b2552)}
.footer .brand{left:44px;top:56px;font-size:42px}
.footer .about-text{left:45px;top:129px;width:330px;font-size:13px;line-height:26.5px;color:#dce3ef}
.footer .contact-line{left:44px;display:flex;align-items:center;gap:12px;font:400 22px "Lato",sans-serif;color:#fff}
.footer .dot{width:20px;height:20px;border-radius:50%;background:var(--orange);display:flex;align-items:center;justify-content:center}
.footer h4{position:absolute;top:69px;font:700 15px "Lato",sans-serif;color:var(--orange)}
.footer h4::after{content:"";position:absolute;left:0;top:34px;width:26px;height:3px;background:#fff}
.footer ul{position:absolute;top:133px;list-style:none}
.footer li{font-size:14px;color:#fff;height:39.3px}
.footer .news{left:875px;top:131px;width:270px;font-size:13px;line-height:26.5px;color:#dce3ef}
.footer .email-in{left:876px;top:201px;width:263px;padding-bottom:8px;border-bottom:1px solid #6f86ad;font-size:13px;color:#fff}
.footer .sub{left:873px;top:257px;width:118px;height:31px;font-size:12px}
.footer .bottom{left:44px;top:379px;width:1112px;height:1px;background:#2f4d80}
.footer .copy{left:52px;top:397px;font-size:13px;color:#c9d3e4}
.footer .soc{top:392px;width:24px;height:24px;border-radius:50%;background:#2b4b84}
</style>
</head>
<body>

<!-- top bar -->
<div class="abs topbar">
  <div class="abs contact" style="left:44px">
    <svg width="12" height="10" viewBox="0 0 12 10"><rect x=".5" y=".5" width="11" height="9" fill="none" stroke="#e6ecf5"/><path d="M.5 .5 6 5l5.5-4.5" fill="none" stroke="#e6ecf5"/></svg>
    info@olvak.example.au
  </div>
  <div class="abs contact" style="left:222px">
    <svg width="8" height="13" viewBox="0 0 8 13"><rect x=".5" y=".5" width="7" height="12" rx="1.5" fill="none" stroke="#e6ecf5"/></svg>
    1800 555 019
  </div>
  <div class="abs staff"><span>
    <svg width="18" height="18" viewBox="0 0 18 18"><circle cx="9" cy="9" r="9" fill="#fff"/><circle cx="9" cy="7" r="3" fill="#f39322"/><path d="M3.5 14.5c1.5-2.5 9.5-2.5 11 0" fill="#f39322"/></svg>
    STAFF LOGIN</span>
    <div class="abs social" style="left:292px"></div>
    <div class="abs social" style="left:325px"></div>
  </div>
</div>

<!-- header -->
<header class="abs header">
  <div class="abs brand" style="left:32px;top:20px"><span class="mark"></span>OLVAK</div>
  <nav class="nav">
    <a class="active" style="left:492px">HOME</a>
    <a style="left:569px">HEATING &amp; COOLING +</a>
    <a style="left:760px">OUR STORY</a>
    <a style="left:881px">SUPPORT</a>
  </nav>
  <a class="abs btn-book">BOOK APPOINTMENT</a>
</header>

<!-- hero -->
<section class="abs hero">
  <div class="abs" role="img" aria-label="Modern house at dusk in deep blue tones" style="inset:0;background:radial-gradient(ellipse at 35% 70%,rgba(70,110,170,.35),transparent 60%)"></div>
  <h1 class="abs">Save Upto <b>70%</b></h1>
  <h2 class="abs">ELECTRICITY COST</h2>
  <a class="abs btn-orange">READ MORE</a>
  <div class="abs product" role="img" aria-label="Two white heat pump water heater units"></div>
</section>

<!-- about -->
<section class="abs about">
  <div class="abs photo" role="img" aria-label="Smiling consultant in a suit meeting a client at a desk"></div>
  <div class="abs eyebrow">AN OVERVIEW ABOUT</div>
  <div class="abs brand"><span class="mark"></span>OLVAK</div>
  <p class="abs">OLVAK is a company dedicated to manufacturing and installing energy-efficient products that reduce energy consumption, save costs, and promote sustainability. Our mission is to help individuals and businesses reduce their carbon footprint while also enhancing their comfort and quality of life. Our story began with a group of like-minded individuals who saw the urgent need to address climate change and the impact of energy consumption on the environment.</p>
  <div class="abs rebate">FULLY COMPLIANT WITH ALL GOVERNMENT REBATES</div>
  <div class="abs badge" style="left:612px;width:113px;height:113px;background:#1f6b4e;border:5px solid #c9a13d"></div>
  <div class="abs badge" style="left:765px;width:127px;height:113px;background:#2c4e93;border:4px solid #fff;box-shadow:0 0 0 1px #ccc"></div>
  <div class="abs badge" style="left:936px;width:117px;height:117px;background:#fff;box-shadow:0 2px 6px rgba(0,0,0,.15)"></div>
</section>

<!-- heating & cooling -->
<div class="abs solutions-bg" role="img" aria-label="Night-time street scene tinted blue"></div>
<section class="solutions">
  <div class="abs eyebrow">OFFERING SOLUTIONS FOR</div>
  <h2 class="abs"><span class="mark"></span>HEATING &amp; COOLING</h2>
  <div class="abs lead">Please select from a category below that best suits your requirements.</div>
  <div class="abs card">
    <div class="tile" style="left:50px;top:58px;background:linear-gradient(180deg,#b9a58e,#8a7866 60%,#6d6a66)" role="img" aria-label="Heat pump unit beside a brick wall"></div>
    <div class="tile-label" style="left:60px;top:329px">Heat Pump</div>
    <div class="tile" style="left:546px;top:58px;background:linear-gradient(180deg,#cbbfb1,#a99883 60%,#8d7e6d)" role="img" aria-label="Family relaxing on a sofa under a wall air conditioner"></div>
    <div class="tile-label" style="left:546px;top:329px">Air Conditioners</div>
    <div class="tile" style="left:50px;top:396px;background:linear-gradient(180deg,#2f4f25,#6f8f6a 50%,#2aa3a0)" role="img" aria-label="Technician servicing a pool heat pump beside a swimming pool"></div>
    <div class="tile-label" style="left:50px;top:667px">Swimming Pool Heat Pump</div>
    <div class="tile" style="left:546px;top:396px;background:linear-gradient(180deg,#e8e9ea,#f3f3f3 60%,#6f9a3e)" role="img" aria-label="Outdoor monoblock heat pump unit on a lawn"></div>
    <div class="tile-label" style="left:554px;top:667px">Monoblock Heat Pump</div>
  </div>
</section>

<!-- testimonials -->
<section class="abs testimonials">
  <div class="abs eyebrow">CLIENT TESTIMONIALS</div>
  <h3 class="abs">What People Are Saying About</h3>
  <div class="abs rule"></div>
  <div class="quote-item">
    <div class="avatar" role="img" aria-label="Portrait of Maya Trent" style="left:67px;top:203px"></div>
    <div class="name" style="left:66px;top:306px">Maya Trent</div>
    <p style="left:181px;top:203px">Lorem ipsum dolor sit amet, consectetur adtipiscing elit, sed do eiusmod tempor incididunt ut labore et dolore magna aliqua. Quis ipsum suspendisse ultrices gravida. Risus commodo viverra maecenas accumsan lacus vel facilisis.</p>
  </div>
  <div class="abs divider"></div>
  <div class="quote-item">
    <div class="avatar" role="img" aria-label="Portrait of Lena Harrow" style="left:67px;top:416px"></div>
    <div class="name" style="left:66px;top:519px">Lena Harrow</div>
    <p style="left:181px;top:416px">Lorem ipsum dolor sit amet, consectetur adtipiscing elit, sed do eiusmod tempor incididunt ut labore et dolore magna aliqua. Quis ipsum suspendisse ultrices gravida. Risus commodo viverra maecenas accumsan lacus vel facilisis.</p>
  </div>
</section>
<div class="abs quote-head"><small>Quick Enquiry</small><strong>GET AN INSTANT QUOTE</strong></div>
<form class="abs quote-form">
  <p>Lorem Ipsum is simply dummy text of the printing and typesetting industry has been the industry's standard dummy when an unknown printer.</p>
  <div class="field" style="left:28px;top:116px;width:266px;height:57px">Your Name</div>
  <div class="field" style="left:308px;top:116px;width:271px;height:57px">Email</div>
  <div class="field" style="left:28px;top:195px;width:266px;height:56px">Phone</div>
  <div class="field" style="left:309px;top:195px;width:266px;height:56px">Requirement</div>
  <div class="field" style="left:28px;top:274px;width:547px;height:131px">Other Details</div>
  <a class="btn-orange">SEND A MESSAGE</a>
</form>

<!-- footer -->
<footer class="abs footer">
  <div class="abs brand"><span class="mark"></span>OLVAK</div>
  <p class="abs about-text">OLVAK is a company dedicated to manufacturing and installing energy-efficient products that reduce energy consumption, save costs, and promote sustainability. Our mission is to help individuals and businesses reduce their carbon footprint while also enhancing their comfort and quality of life.</p>
  <div class="abs contact-line" style="top:294px"><span class="dot"><svg width="10" height="10" viewBox="0 0 10 10"><path d="M2 1l2 2-1 1.5c.8 1.5 1.5 2.2 2.5 2.5L7 6l2 2-1.5 1.5C4.5 9 1 5.5.5 2.5z" fill="#fff"/></svg></span>1800 555 019</div>
  <div class="abs contact-line" style="top:330px"><span class="dot"><svg width="10" height="8" viewBox="0 0 10 8"><rect x=".5" y=".5" width="9" height="7" fill="none" stroke="#fff"/><path d="M.5.5 5 4 9.5.5" fill="none" stroke="#fff"/></svg></span>info@olvak.example.au</div>

  <h4 style="left:438px">Heating &amp; Cooling Services</h4>
  <ul style="left:441px"><li>Heat Pump</li><li>Air Conditioners</li><li>Swimming Pool Heat Pump</li><li>Monoblock Heat Pump</li></ul>

  <h4 style="left:695px">Usefull Links</h4>
  <ul style="left:699px"><li>Home</li><li>Our Story</li><li>Support</li><li>Book Appointment</li></ul>

  <h4 style="left:875px">Get in Touch</h4>
  <p class="abs news">Enter your email address to register to our newsletter subscription</p>
  <div class="abs email-in">Your Email</div>
  <a class="abs btn-orange sub">SUBSCRIBE</a>

  <div class="abs bottom"></div>
  <div class="abs copy">© Copyright 2024 OLVAK &nbsp;-&nbsp;&nbsp; All rights reserved.</div>
  <div class="abs soc" style="left:1009px"></div>
  <div class="abs soc" style="left:1042px"></div>
  <div class="abs soc" style="left:1076px"></div>
  <div class="abs soc" style="left:1108px"></div>
</footer>

</body>
</html>
```